Business Card Design Project

Im an electrician and my company name is Kestrel Electrical
My main work is installing Lighting and Power Points, Home Theater Systems, TVS, Phones and Data
Im looking a business card, something nice, clean, modern and not to cluttered
Im open to sugestions
I dont mind if the "Services" is on the back on the business card
colours black, grey, white or the blue colour of my logo are prefered but not compulsory
any questions just message me
and please make it so if i need to edit the writing can do it easy. maybe by making it a seperate layer ?
My Details are.
Name - Peter Halloran
Job Title - Licenced Electrician
Mobile - 027 583 2174
Email - peter@kestrelelectrical.co.nz
Web - www.kestrelelectrical.co.nz
Services
Residential / Commercial
Lighting & Power
Heating & Ventilation
Automation
Phone & Data
Home Cinema
Sound Systems
TV, Antenna & Satellite
Digital Upgrades

```html
<!DOCTYPE html>
<html lang="en">
<head>
<meta charset="utf-8">
<title>Kestrel Electrical – Business Card</title>
<link rel="stylesheet" href="https://fonts.googleapis.com/css2?family=PT+Sans:wght@400;700&family=Questrial&display=swap">
<style>
  :root {
    --backdrop: #d9dcde;
    --card-dark: #1c1c1c;
    --card-light: #ffffff;
    --brand-blue: #00a3c4;
    --ink: #1a1a1a;
    --ink-soft: #333333;
    --card-shadow: 0 3px 8px rgba(0,0,0,0.25);
  }
  * { margin: 0; padding: 0; box-sizing: border-box; }
  html, body {
    width: 1200px;
    height: 603px;
    overflow: hidden;
    background: var(--backdrop);
  }
  .canvas {
    position: relative;
    width: 1200px;
    height: 603px;
  }
  .card {
    position: absolute;
    top: 142px;
    width: 548px;
    height: 334px;
    border-radius: 16px;
    overflow: hidden;
    box-shadow: var(--card-shadow);
  }
  .card--back {
    left: 33px;
    background: var(--card-dark);
    display: flex;
    align-items: center;
    justify-content: center;
  }
  .card--front {
    left: 625px;
    background: var(--card-light);
  }

  /* Brand lockup */
  .brand {
    display: flex;
    align-items: center;
    gap: 12px;
    margin-top: -10px;
  }
  .brand__square {
    width: 22px;
    height: 22px;
    background: var(--brand-blue);
  }
  .brand__name {
    font-family: "PT Sans", sans-serif;
    font-weight: 700;
    font-size: 30px;
    letter-spacing: 1px;
    text-transform: uppercase;
    color: var(--brand-blue);
  }

  /* Front decoration */
  .accent-band {
    position: absolute;
    inset: 0;
    width: 100%;
    height: 100%;
  }

  .contact-block {
    position: absolute;
    left: 40px;
    top: 145px;
  }
  .person__name {
    font-family: "Questrial", sans-serif;
    font-variant-caps: small-caps;
    font-size: 21px;
    letter-spacing: 1px;
    color: var(--ink);
    line-height: 1;
  }
  .person__title {
    font-family: "PT Sans", sans-serif;
    font-size: 14.5px;
    color: var(--ink-soft);
    margin-top: 8px;
  }
  .contact-list {
    list-style: none;
    margin-top: 26px;
  }
  .contact-list__item {
    display: flex;
    align-items: center;
    gap: 8px;
    height: 20px;
    margin-bottom: 12px;
    font-family: "PT Sans", sans-serif;
    font-size: 15px;
    color: var(--ink);
  }
  .contact-icon {
    width: 20px;
    height: 20px;
    flex: none;
  }
</style>
</head>
<body>
  <main class="canvas">
    <section class="card card--back" aria-label="Card back">
      <div class="brand">
        <span class="brand__square" aria-hidden="true"></span>
        <span class="brand__name">Kestrel Electrical</span>
      </div>
    </section>

    <section class="card card--front" aria-label="Card front">
      <svg class="accent-band" viewBox="0 0 548 334" aria-hidden="true">
        <polygon points="478,0 560,0 475,334 393,334" fill="var(--brand-blue)"/>
      </svg>

      <div class="contact-block">
        <h1 class="person__name">Peter Halloran</h1>
        <p class="person__title">Licenced Electrician</p>

        <ul class="contact-list">
          <li class="contact-list__item">
            <svg class="contact-icon" viewBox="0 0 20 20" aria-hidden="true">
              <rect width="20" height="20" rx="4" fill="var(--ink)"/>
              <path d="M6.2 4.5l2 2.3-1.1 1.4c.8 1.7 2 2.9 3.7 3.7l1.4-1.1 2.3 2-1 1.9c-4.6-.4-8.2-4-8.6-8.6z" fill="#fff"/>
            </svg>
            <span>027 583 2174</span>
          </li>
          <li class="contact-list__item">
            <svg class="contact-icon" viewBox="0 0 20 20" aria-hidden="true">
              <rect width="20" height="20" rx="4" fill="var(--ink)"/>
              <rect x="4.5" y="6" width="11" height="8" fill="none" stroke="#fff" stroke-width="1.3"/>
              <path d="M4.5 6l5.5 4.3L15.5 6" fill="none" stroke="#fff" stroke-width="1.3"/>
            </svg>
            <span>peter@kestrelelectrical.co.nz</span>
          </li>
          <li class="contact-list__item">
            <svg class="contact-icon" viewBox="0 0 20 20" aria-hidden="true">
              <rect width="20" height="20" rx="4" fill="var(--ink)"/>
              <g fill="none" stroke="#fff" stroke-width="1.1">
                <circle cx="10" cy="10" r="5.6"/>
                <ellipse cx="10" cy="10" rx="2.4" ry="5.6"/>
                <path d="M4.4 10h11.2M5.3 7h9.4M5.3 13h9.4"/>
              </g>
            </svg>
            <span>www.kestrelelectrical.co.nz</span>
          </li>
        </ul>
      </div>
    </section>
  </main>
</body>
</html>
```